Interior Design/ decoration business card design

This card is for my Interior Design and Decoration business and later I will also be selling homewares. I would like the card to be very simple in design and like either white, duck egg blue , aquas or metallics on a flat mat card excellent quality card. It needs to be well designed as that is my field. I dont like fuss, the simpler the better. I would like a styalised wren under the name wren if possible. SIMPLE, STYLISH, CLASSIC, TASTEFUL

Target Market(s)

40 + year olds who are building or rennovating.

Industry/Entity Type

Business

Contact Information for Business Card

Wren
styling, design, homeware

Marnie Tolland
p 0427316958
e marnie@wrenliving.com.au
w wrenliving.com.au

Requirements
Must have
• very simple, stylish, classic, sophisticated. Simple and easy to read text that is a print similar to attached image. I like simple round A's though not as in attached image.

Double sided. It wont save as double sided for some reason!!
Should not have
• not too much colour, No animated / cartoon pictures.

```html
<!DOCTYPE html>
<html lang="en">
<head>
<meta charset="utf-8">
<title>Wren – Business Card</title>
<link href="https://fonts.googleapis.com/css2?family=Open+Sans:wght@300;400;600&display=swap" rel="stylesheet">
<style>
  :root {
    --backdrop: #3a302a;
    --card: #2a2320;
    --mint: #b6d5cd;
    --tagline: #b3ada7;
    --label: #f1efec;
  }
  html, body {
    margin: 0;
    padding: 0;
    width: 1200px;
    height: 1000px;
    overflow: hidden;
    background: var(--backdrop);
    font-family: "Open Sans", sans-serif;
  }
  .canvas {
    position: relative;
    width: 1200px;
    height: 1000px;
  }
  .card {
    position: absolute;
    left: 290px;
    width: 610px;
    height: 377px;
    background: var(--card);
    box-shadow: 6px 8px 18px rgba(0, 0, 0, 0.35);
  }
  .card--front { top: 103px; }
  .card--back { top: 518px; }

  .brand-name {
    position: absolute;
    left: 0;
    right: 0;
    top: 100px;
    margin: 0;
    text-align: center;
    font-weight: 300;
    font-size: 64px;
    letter-spacing: 2px;
    line-height: 1;
    color: var(--mint);
  }
  .tagline {
    position: absolute;
    left: 0;
    right: 0;
    top: 289px;
    margin: 0;
    text-align: center;
    font-weight: 300;
    font-size: 21px;
    letter-spacing: 0.5px;
    color: var(--tagline);
  }
  .tagline .dot {
    display: inline-block;
    width: 4px;
    height: 4px;
    border-radius: 50%;
    background: var(--tagline);
    vertical-align: middle;
    margin: 0 3px;
  }

  .person-name {
    position: absolute;
    left: 69px;
    top: 102px;
    margin: 0;
    font-weight: 600;
    font-size: 26px;
    letter-spacing: 1px;
    color: var(--mint);
  }
  .contact-list {
    position: absolute;
    left: 125px;
    top: 168px;
    margin: 0;
    display: grid;
    grid-template-columns: 114px auto;
    row-gap: 17px;
    font-size: 19px;
    letter-spacing: 1px;
    line-height: 24px;
  }
  .contact-list dt {
    font-weight: 600;
    color: var(--label);
  }
  .contact-list dd {
    margin: 0;
    font-weight: 600;
    color: var(--mint);
  }
</style>
</head>
<body>
  <main class="canvas">
    <section class="card card--front" aria-label="Card front">
      <h1 class="brand-name">wren</h1>
      <p class="tagline">decoration<span class="dot"></span>styling<span class="dot"></span>homeware</p>
    </section>

    <section class="card card--back" aria-label="Card back">
      <h2 class="person-name">Marnie Tolland</h2>
      <dl class="contact-list">
        <dt>phone</dt><dd>0427316958</dd>
        <dt>email</dt><dd>marnie@wrenliving.com.au</dd>
        <dt>web</dt><dd>wrenliving.com.au</dd>
      </dl>
    </section>
  </main>
</body>
</html>
```